Family Owned Construction Company Needs Modern Business Cards

We need a new design for our business cards. We are a family owned construction company, Brantwell Construction, based in Mendon, Vermont and would like to add in our new logo and find a more modern look. We also want to use our old to make sure people know who we are. We do site development, highway, environmental, demolition, utility and aggregate.

Contact Information for Business Card

We want to have the office address, 418 Quarry Ridge Road, Alder Falls, NH 03901 and our phone (802) 555-0137 and fax (802) 555-0164 on there as well. Our website is www.brantwellinc.example. There should be a place for the person's name, title, cell number, and email address on the card. Words that we would like to be associated with our company are honesty, predictable, reliable, integrity, dedicated, built right quality, consistent, whatever it takes, and innovation. Safety is also very important to us.

Font styles to use
Serif
Sans Serif
Other font styles liked:
• Square 721 Extented

Colors
0255a3
ffffff

Requirements
Must have
• Office address, phone number and fax number. New logo with excavator
Nice to have
• That we do site development, highway, environmental, demolition, utility, and aggregate. Both logos

```html
<!DOCTYPE html>
<html lang="en">
<head>
<meta charset="utf-8">
<title>Brantwell Construction – Business Cards</title>
<link href="https://fonts.googleapis.com/css2?family=Exo+2:wght@600&family=Source+Sans+3:wght@400&display=swap" rel="stylesheet">
<style>
  :root {
    --navy: #0f2c66;
    --navy-deep: #0b295f;
    --navy-pattern: #1a3d78;
    --white: #ffffff;
    --stage-top: #9d9d9d;
    --stage-bottom: #7f7f7f;
    --rule: #3b4f80;
  }
  * { margin: 0; padding: 0; box-sizing: border-box; }
  html, body { width: 1200px; height: 900px; overflow: hidden; }
  body {
    position: relative;
    background: linear-gradient(to bottom, var(--stage-top), var(--stage-bottom));
    font-family: "Source Sans 3", sans-serif;
    color: var(--navy);
  }
  .card {
    position: absolute;
    top: 306px;
    width: 439px;
    height: 271px;
    border-radius: 10px;
    overflow: hidden;
  }
  .card--front { left: 149px; background: var(--white); }
  .card--back { left: 609px; background: var(--navy-deep); }

  .brand {
    position: absolute;
    display: flex;
    align-items: center;
    gap: 10px;
    transform: translate(-50%, -50%);
    font-family: "Source Sans 3", sans-serif;
    font-weight: 400;
    font-size: 24px;
    line-height: 1.1;
    white-space: nowrap;
  }
  .brand__mark { width: 32px; height: 32px; flex: none; }
  .card--front .brand { left: 131px; top: 136px; color: var(--navy); }
  .card--front .brand__mark { background: var(--navy); }
  .card--back .brand { left: 221px; top: 136px; color: var(--white); }
  .card--back .brand__mark { background: var(--white); }

  .divider {
    position: absolute;
    left: 238px; top: 62px;
    width: 1px; height: 148px;
    background: var(--rule);
  }
  .details { position: absolute; left: 258px; top: 57px; }
  .details__name {
    font-family: "Exo 2", sans-serif;
    font-weight: 600;
    font-size: 16.5px;
    letter-spacing: 0.3px;
    line-height: 1.1;
    text-transform: uppercase;
  }
  .details__title { font-size: 12.5px; line-height: 1.2; }
  .details__address { font-size: 12.5px; line-height: 16px; margin-top: 6px; }
  .contact { list-style: none; margin-top: 6px; }
  .contact li {
    display: flex; align-items: center; gap: 6px;
    font-size: 12.5px; line-height: 15.8px;
  }
  .contact svg { width: 9px; height: 9px; fill: var(--navy); flex: none; }

  .back-pattern {
    position: absolute; inset: 0;
    background: var(--navy-pattern);
    opacity: 0.6;
  }
</style>
</head>
<body>

<section class="card card--front" aria-label="Business card front">
  <div class="brand">
    <span class="brand__mark"></span>
    <span>Brantwell<br>Construction</span>
  </div>
  <div class="divider"></div>
  <div class="details">
    <h1 class="details__name">Daniel Mercer</h1>
    <p class="details__title">Managing Director</p>
    <p class="details__address">418 Quarry Ridge Road,<br>Alder Falls, NH 03901</p>
    <ul class="contact">
      <li><svg viewBox="0 0 10 10"><path d="M1 4c0-2 2-3 4-3s4 1 4 3H7V3H3v1zM2 5h6l1 4H1z"/></svg>(802) 555-0137</li>
      <li><svg viewBox="0 0 10 10"><path d="M2.5 0h5v10h-5zM3.5 1v7h3V1z"/></svg>(802) 555-0191</li>
      <li><svg viewBox="0 0 10 10"><path d="M2 0h5v3H2zM1 3h8v7H1zM3 5v1h4V5zM3 7v1h4V7z"/></svg>(802) 555-0164</li>
      <li><svg viewBox="0 0 10 10"><path d="M0 2h10v6H0zM1 3l4 3 4-3v-.5H1z"/></svg>info@brantwellinc.example</li>
      <li><svg viewBox="0 0 10 10"><circle cx="5" cy="5" r="5"/></svg>www.brantwellinc.example</li>
    </ul>
  </div>
</section>

<section class="card card--back" aria-label="Business card back">
  <div class="back-pattern" role="img" aria-label="Faint repeating brand pattern across the card"></div>
  <div class="brand">
    <span class="brand__mark"></span>
    <span>Brantwell<br>Construction</span>
  </div>
</section>

</body>
</html>
```